Brochure Design Project

Architectural photography and virtual tour provider for local and national real estate markets. You can use my website for design and image needs. www.larkfieldvistas.com

```html
<!DOCTYPE html>
<html lang="en">
<head>
<meta charset="utf-8">
<title>Larkfield Vistas – Brochure Cover</title>
<link rel="stylesheet" href="https://fonts.googleapis.com/css2?family=Merriweather:wght@400&family=Open+Sans:wght@600&family=Montserrat:wght@400;900&display=swap">
<style>
  :root {
    --stage: #e4e4e4;
    --paper: #ffffff;
    --ink: #2a2a2a;
    --brand-blue: #1b4fa3;
    --brand-green: #3aa447;
  }
  * { margin: 0; padding: 0; box-sizing: border-box; }
  html, body { width: 1200px; height: 790px; overflow: hidden; }
  body { background: var(--stage); position: relative; }

  .cover {
    position: absolute; left: 340px; top: 25px;
    width: 520px; height: 740px;
    background: var(--paper);
    box-shadow: 0 6px 18px rgba(0,0,0,.12);
  }

  .brand { position: absolute; left: 70px; top: 36px; width: 380px; }
  .brand-row { display: flex; align-items: center; gap: 12px; }
  .brand-mark { width: 22px; height: 22px; background: var(--brand-green); flex: none; }
  .brand-name {
    font-family: "Merriweather", Georgia, serif;
    font-size: 24px; color: var(--ink); letter-spacing: .3px;
  }
  .brand-tagline {
    font-family: "Merriweather", Georgia, serif;
    font-size: 9.5px; color: var(--ink);
    text-align: right; padding-right: 40px; margin-top: 2px;
  }
  .brand-former {
    font-family: "Open Sans", Arial, sans-serif; font-weight: 600;
    font-size: 10.5px; color: var(--brand-blue); margin-top: 6px; padding-left: 10px;
  }

  .tile { position: absolute; }
  .tile--dining   { left: 30px;  top: 150px; width: 220px; height: 85px;  background: linear-gradient(135deg,#f1efec,#b9b3ab 60%,#5b4f47); }
  .tile--bedroom  { left: 256px; top: 110px; width: 124px; height: 95px;  background: linear-gradient(160deg,#e8e4df,#8fa6b8 50%,#b3282b); }
  .tile--great    { left: 386px; top: 110px; width: 104px; height: 80px;  background: linear-gradient(150deg,#d8c4a6,#8a5a32 55%,#5a3a22); }
  .tile--kitchen  { left: 30px;  top: 241px; width: 100px; height: 80px;  background: linear-gradient(160deg,#efe7df,#b8622f 55%,#7a3a1c); }
  .tile--lounge   { left: 136px; top: 241px; width: 114px; height: 170px; background: linear-gradient(170deg,#e9e3da,#b9a994 55%,#4b4440); }
  .tile--poolhouse{ left: 256px; top: 211px; width: 234px; height: 170px; background: linear-gradient(180deg,#5a96d8 0%,#d9b8a6 35%,#4f8a3d 62%,#3dbbe0 80%,#8a8a6a); }
  .tile--cellar   { left: 30px;  top: 327px; width: 100px; height: 84px;  background: linear-gradient(160deg,#c9a27a,#6a3f24 55%,#3a2418); }
  .tile--fountain { left: 30px;  top: 417px; width: 130px; height: 95px;  background: linear-gradient(180deg,#6e7fb8,#3f7fc4 50%,#c9a243); }
  .tile--bath     { left: 166px; top: 417px; width: 120px; height: 95px;  background: linear-gradient(160deg,#7a6a5a,#d9d2c6 50%,#4a3a2e); }
  .tile--evening  { left: 292px; top: 387px; width: 198px; height: 125px; background: linear-gradient(180deg,#5b78a8,#2c3a5a 45%,#c99a3e 60%,#1e2636); }

  .headline {
    position: absolute; left: 0; right: 0; top: 548px; text-align: center;
    font-family: "Montserrat", Arial, sans-serif; font-weight: 900;
    font-size: 86px; line-height: 1; color: var(--brand-blue); letter-spacing: 1px;
  }
  .subline {
    position: absolute; left: 60px; right: 0; top: 640px; text-align: center;
    font-family: "Montserrat", Arial, sans-serif; font-weight: 400;
    font-size: 14px; letter-spacing: 3px; color: var(--brand-blue);
  }
</style>
</head>
<body>
  <main class="cover">
    <header class="brand">
      <div class="brand-row">
        <span class="brand-mark"></span>
        <span class="brand-name">Larkfield Vistas</span>
      </div>
      <p class="brand-tagline">Become noticed...</p>
      <p class="brand-former">formerly Canyon Valley Home Tours</p>
    </header>

    <section class="gallery">
      <div class="tile tile--dining" role="img" aria-label="Bright open dining and living room with chandelier"></div>
      <div class="tile tile--bedroom" role="img" aria-label="Bedroom with red bedding and large windows"></div>
      <div class="tile tile--great" role="img" aria-label="Great room with wood beams and wooden floor"></div>
      <div class="tile tile--kitchen" role="img" aria-label="Kitchen with cherry wood cabinets"></div>
      <div class="tile tile--lounge" role="img" aria-label="Living area with coffee table and rug"></div>
      <div class="tile tile--poolhouse" role="img" aria-label="Villa with balcony, palms and swimming pool"></div>
      <div class="tile tile--cellar" role="img" aria-label="Wine cellar tasting room"></div>
      <div class="tile tile--fountain" role="img" aria-label="Backyard fountain at dusk"></div>
      <div class="tile tile--bath" role="img" aria-label="Bathroom vanity with marble counter"></div>
      <div class="tile tile--evening" role="img" aria-label="Hillside home lit up at twilight"></div>
    </section>

    <h1 class="headline">QUALITY</h1>
    <p class="subline">YOU CAN SEE</p>
  </main>
</body>
</html>
```